Endocrinologist needs new stationery

I have a logo from MarkForge and now need stationery with the new logo.

Address: Suite 4, 282 Falcon Street, Ashvale, VIC 3148
Phone: 03 9417 2253
Fax: 03 9417 2255
Website: www.drmaylacorwen.com.au
Email: admin@drmaylacorwen.com.au

```html
<!DOCTYPE html>
<html lang="en">
<head>
<meta charset="utf-8">
<title>Dr Mayla Corwen – Stationery Set</title>
<link rel="stylesheet" href="https://fonts.googleapis.com/css2?family=Open+Sans:wght@400;700&family=Tinos:wght@400;700&display=swap">
<style>
  :root{
    --board:#1f2326;
    --paper:#ffffff;
    --card-grey:#d9dadc;
    --brand-blue:#3b72a8;
    --band-plum:#6b4d64;
    --ink:#555a60;
    --rule:#9aa0a6;
    --label:#ffffff;
  }
  *{box-sizing:border-box;margin:0;padding:0}
  html,body{width:696px;height:1200px;overflow:hidden;background:var(--board)}
  .board{position:relative;width:696px;height:1200px;font-family:"Tinos",serif;color:var(--ink)}
  .label{position:absolute;font-family:"Open Sans",sans-serif;color:var(--label);font-size:12px;line-height:1}
  .label.bold{font-weight:700}
  .sheet{position:absolute;background:var(--paper);overflow:hidden}
  .sheet.band::after{content:"";position:absolute;left:0;right:0;bottom:0;height:var(--band,6px);background:var(--band-plum)}
  .brand{position:absolute;line-height:1}
  .brand-name{font-family:"Tinos",serif;font-weight:400;color:var(--brand-blue);font-size:var(--bs,13px);white-space:nowrap;letter-spacing:.02em}
  .contact{position:absolute;display:flex;align-items:center;font-size:var(--cs,4.6px);line-height:1.6;color:var(--ink);white-space:nowrap}
  .contact .col{padding:0 4px;border-left:.6px solid var(--brand-blue)}
  .contact .col:first-child{padding-left:0;border-left:0}
  .contact .row{display:flex;align-items:center;gap:2px}
  .contact svg{width:1.1em;height:1.1em;fill:var(--ink);flex:none}
  .ruled{position:absolute;border-top:.6px solid #b9bcbf}
  .compliments{position:absolute;right:12px;top:10px;font-family:"Tinos",serif;font-weight:700;color:var(--band-plum);font-size:9px}
  .rx-fields{position:absolute;left:9px;right:9px;top:38px;display:flex;font-size:4.2px;color:var(--brand-blue);gap:3px;border-bottom:.6px solid var(--ink);padding-bottom:7px}
  .rx-fields .dots{flex:1;border-bottom:.5px dotted var(--ink);margin-bottom:1px}
  .rx-fields .dots.short{flex:.35}
  .rx-divider{position:absolute;left:65px;top:53px;height:266px;border-left:.7px solid var(--band-plum)}
  .env-flap{position:absolute;inset:0}
</style>
</head>
<body>
<svg width="0" height="0" style="position:absolute">
  <defs>
    <symbol id="i-phone" viewBox="0 0 10 10"><path d="M2 1l2 2-1 1.2c.6 1.2 1.6 2.2 2.8 2.8L7 6l2 2-1.2 1.2C4.5 9 1 5.5.8 2.2z"/></symbol>
    <symbol id="i-fax" viewBox="0 0 10 10"><path d="M3 1h4v2H3zM1 3.5h8V7H7.5v2h-5V7H1zM3.3 7h3.4v1.3H3.3z"/></symbol>
    <symbol id="i-mail" viewBox="0 0 10 10"><path d="M1 2.5h8v5H1zM1.6 3l3.4 2.5L8.4 3" stroke="#fff" stroke-width=".6"/></symbol>
    <symbol id="i-web" viewBox="0 0 10 10"><circle cx="5" cy="5" r="4"/><path d="M1 5h8M5 1v8M2.2 3h5.6M2.2 7h5.6" stroke="#fff" stroke-width=".5" fill="none"/></symbol>
  </defs>
</svg>

<main class="board">

  <p class="label bold" style="left:57px;top:30px">Business Card_4</p>
  <section class="sheet" style="left:55px;top:58px;width:250px;height:150px;background:var(--card-grey)" aria-label="Business card back">
    <div class="brand" style="left:48px;top:62px;--bs:17px"><div class="brand-name">Dr Mayla Corwen</div></div>
    <div class="ruled" style="left:186px;width:40px;top:76px;border-color:var(--brand-blue)"></div>
  </section>
  <section class="sheet band" style="left:95px;top:220px;width:250px;height:150px;--band:5px" aria-label="Business card front">
    <div class="brand" style="left:14px;top:70px;--bs:14px"><div class="brand-name">Dr Mayla Corwen</div></div>
    <div class="ruled" style="left:14px;right:14px;top:94px;border-color:var(--brand-blue)"></div>
    <div class="contact" style="left:14px;top:102px;--cs:5.6px">
      <div class="col"><div class="row"><svg><use href="#i-phone"/></svg>03 9417 2253</div><div class="row"><svg><use href="#i-fax"/></svg>03 9417 2255</div></div>
      <div class="col"><div class="row"><svg><use href="#i-mail"/></svg>admin@drmaylacorwen.com.au</div><div class="row"><svg><use href="#i-web"/></svg>www.drmaylacorwen.com.au</div></div>
      <div class="col"><div>Suite 4, 282 Falcon Street</div><div>Ashvale, VIC 3148</div></div>
    </div>
  </section>

  <p class="label" style="left:419px;top:25px">Note Pads_4</p>
  <section class="sheet band" style="left:419px;top:47px;width:230px;height:162px" aria-label="Note pad">
    <div class="brand" style="left:9px;top:10px;--bs:11px"><div class="brand-name">Dr Mayla Corwen</div></div>
    <div class="ruled" style="left:9px;width:154px;top:32px;border-color:var(--brand-blue)"></div>
    <div class="contact" style="left:9px;top:37px;--cs:4.1px">
      <div class="col"><div class="row"><svg><use href="#i-phone"/></svg>03 9417 2253</div><div class="row"><svg><use href="#i-fax"/></svg>03 9417 2255</div></div>
      <div class="col"><div class="row"><svg><use href="#i-mail"/></svg>admin@drmaylacorwen.com.au</div><div class="row"><svg><use href="#i-web"/></svg>www.drmaylacorwen.com.au</div></div>
      <div class="col"><div>Suite 4, 282 Falcon Street</div><div>Ashvale, VIC 3148</div></div>
    </div>
    <div class="ruled" style="left:8px;right:8px;top:69px"></div>
    <div class="ruled" style="left:8px;right:8px;top:80px"></div>
    <div class="ruled" style="left:8px;right:8px;top:90px"></div>
    <div class="ruled" style="left:8px;right:8px;top:101px"></div>
    <div class="ruled" style="left:8px;right:8px;top:111px"></div>
    <div class="ruled" style="left:8px;right:8px;top:122px"></div>
    <div class="ruled" style="left:8px;right:8px;top:132px"></div>
    <div class="ruled" style="left:8px;right:8px;top:143px"></div>
  </section>

  <p class="label" style="left:419px;top:238px">Comp Slips_4</p>
  <section class="sheet band" style="left:419px;top:260px;width:245px;height:116px" aria-label="Compliments slip">
    <p class="compliments">With Compliments</p>
    <div class="brand" style="left:9px;top:59px;--bs:11px"><div class="brand-name">Dr Mayla Corwen</div></div>
    <div class="ruled" style="left:9px;width:164px;top:83px;border-color:var(--brand-blue)"></div>
    <div class="contact" style="left:9px;top:88px;--cs:4.3px">
      <div class="col"><div class="row"><svg><use href="#i-phone"/></svg>03 9417 2253</div><div class="row"><svg><use href="#i-fax"/></svg>03 9417 2255</div></div>
      <div class="col"><div class="row"><svg><use href="#i-mail"/></svg>admin@drmaylacorwen.com.au</div><div class="row"><svg><use href="#i-web"/></svg>www.drmaylacorwen.com.au</div></div>
      <div class="col"><div>Suite 4, 282 Falcon Street</div><div>Ashvale, VIC 3148</div></div>
    </div>
  </section>

  <p class="label" style="left:57px;top:428px">Letterhead_4</p>
  <section class="sheet band" style="left:57px;top:452px;width:276px;height:357px" aria-label="Letterhead">
    <div class="brand" style="left:9px;top:295px;--bs:12px"><div class="brand-name">Dr Mayla Corwen</div></div>
    <div class="ruled" style="left:9px;width:180px;top:321px;border-color:var(--ink)"></div>
    <div class="contact" style="left:9px;top:327px;--cs:4.7px">
      <div class="col"><div class="row"><svg><use href="#i-phone"/></svg>03 9417 2253</div><div class="row"><svg><use href="#i-fax"/></svg>03 9417 2255</div></div>
      <div class="col"><div class="row"><svg><use href="#i-mail"/></svg>admin@drmaylacorwen.com.au</div><div class="row"><svg><use href="#i-web"/></svg>www.drmaylacorwen.com.au</div></div>
      <div class="col"><div>Suite 4, 282 Falcon Street</div><div>Ashvale, VIC 3148</div></div>
    </div>
  </section>

  <p class="label" style="left:378px;top:428px">Prescription Pad_4</p>
  <section class="sheet band" style="left:378px;top:452px;width:277px;height:357px" aria-label="Prescription pad">
    <div class="brand" style="left:9px;top:10px;--bs:13px"><div class="brand-name">Dr Mayla Corwen</div></div>
    <div class="rx-fields"><span>Name</span><span class="dots"></span><span>Age</span><span class="dots short"></span><span>Sex</span><span class="dots short"></span><span>Date</span><span class="dots short"></span></div>
    <div class="rx-divider"></div>
    <div class="ruled" style="left:9px;width:180px;top:323px;border-color:var(--ink)"></div>
    <div class="contact" style="left:9px;top:328px;--cs:4.7px">
      <div class="col"><div class="row"><svg><use href="#i-phone"/></svg>03 9417 2253</div><div class="row"><svg><use href="#i-fax"/></svg>03 9417 2255</div></div>
      <div class="col"><div class="row"><svg><use href="#i-mail"/></svg>admin@drmaylacorwen.com.au</div><div class="row"><svg><use href="#i-web"/></svg>www.drmaylacorwen.com.au</div></div>
      <div class="col"><div>Suite 4, 282 Falcon Street</div><div>Ashvale, VIC 3148</div></div>
    </div>
  </section>

  <p class="label" style="left:57px;top:854px">ENV Front_4</p>
  <section class="sheet band" style="left:56px;top:879px;width:284px;height:123px" aria-label="Envelope front">
    <div class="brand" style="left:9px;top:64px;--bs:11px"><div class="brand-name">Dr Mayla Corwen</div></div>
    <div class="ruled" style="left:9px;width:98px;top:90px;border-color:var(--brand-blue)"></div>
    <div class="contact" style="left:9px;top:95px;--cs:4.3px"><div class="col"><div>Suite 4, 282 Falcon Street</div><div>Ashvale, VIC 3148</div></div></div>
  </section>

  <p class="label" style="left:365px;top:854px">ENV Back_4</p>
  <section class="sheet" style="left:365px;top:879px;width:282px;height:123px" aria-label="Envelope back">
    <svg class="env-flap" viewBox="0 0 282 123" preserveAspectRatio="none"><path d="M0 0h282c-6 14-10 18-22 20L146 43c-3 .6-7 .6-10 0L22 20C10 18 5 14 0 0z" fill="#c9cacc"/></svg>
  </section>

  <p class="label" style="left:200px;top:1033px">Email signature_4</p>
  <section class="sheet band" style="left:200px;top:1058px;width:299px;height:99px;--band:11px" aria-label="Email signature">
    <div class="brand" style="left:15px;top:23px;--bs:13px"><div class="brand-name">Dr Mayla Corwen</div></div>
    <div class="ruled" style="left:15px;width:198px;top:54px;border-color:var(--brand-blue)"></div>
    <div class="contact" style="left:15px;top:60px;--cs:5.2px">
      <div class="col"><div class="row"><svg><use href="#i-phone"/></svg>03 9417 2253</div><div class="row"><svg><use href="#i-fax"/></svg>03 9417 2255</div></div>
      <div class="col"><div class="row"><svg><use href="#i-mail"/></svg>admin@drmaylacorwen.com.au</div><div class="row"><svg><use href="#i-web"/></svg>www.drmaylacorwen.com.au</div></div>
      <div class="col"><div>Suite 4, 282 Falcon Street</div><div>Ashvale, VIC 3148</div></div>
    </div>
  </section>

</main>
</body>
</html>
```